Logo & Visitenkarten-Design für technische Innovationen
Zielgruppe
Mein Leistungsangebot richtet sich an Unternehmen im nationalen und internationalen Bereich mit der Zielsetzung bestehende technologische Innovationen aus dem IoT Bereich (im Wesentlichen verbunden mit RFID und NFC Technologie) in erfolgreiche Geschäftskonzepte zu transformieren. Dabei richtet sich meine Tätigkeit auch darauf, verschiedene Unternehmen mit deckungsgleichen Interessen zusammenzubringen und so ein erfolgreiche Partnerschaft zu ermöglichen. Im Logo kann daher auch auf das Thema Netzwerk, Partnering und Kooperation eingegangen werden.
Aufgabenstellung
Sie meine Angaben bereits oben.
Generell bevorzuge ich eher ein helles Logo und kein design auf einen dunklen Untergrund/Hintergrund.
Angesprochen werden im Wesentlichen zwei Kundengruppen:
1) Innovative Technologiefirmen, oftmals Start-Ups, die ihr Produkt jetzt monetarisieren wollen und entsprechende Kunden bzw. Partner suchen
2) Kunden aus dem Retail Segment, hier zumeist aus dem Fashion-Bereich, die diese Produktinnovationen nutzen wollen, um eine zielgerichtetere Kundenkommunikation zu erreichen.

```html
<!DOCTYPE html>
<html lang="de">
<head>
<meta charset="utf-8">
<title>KD Velatrans – Visitenkarte</title>
<link rel="stylesheet" href="https://fonts.googleapis.com/css2?family=Montserrat:wght@300;400&display=swap">
<style>
  :root {
    --backdrop: #e7e4e0;
    --card: #f7f5f1;
    --brand-red: #8c2b30;
    --logo-grey: #6f6f6f;
    --text-grey: #7a7a7a;
    --title-grey: #b3b0ab;
  }
  * { margin: 0; padding: 0; box-sizing: border-box; }
  html, body {
    width: 1200px; height: 800px; overflow: hidden;
    background: var(--backdrop);
    font-family: "Montserrat", sans-serif;
  }
  .card {
    position: absolute; left: 100px; top: 77px;
    width: 1000px; height: 646px;
    background: var(--card);
    box-shadow: 0 10px 30px rgba(0,0,0,.12);
  }
  .brand {
    position: absolute; left: 70px; top: 190px;
    width: 470px;
    display: flex; align-items: center; gap: 26px;
  }
  .brand-mark { width: 140px; height: 140px; flex: none; }
  .brand-name {
    font-weight: 400; font-size: 26px; letter-spacing: 4px;
    color: var(--logo-grey); text-transform: uppercase;
    white-space: nowrap;
  }
  .contact {
    position: absolute; left: 590px; top: 232px;
    color: var(--text-grey); font-weight: 300;
  }
  .contact-name {
    font-weight: 400; font-size: 30px; color: var(--brand-red);
    text-transform: uppercase; line-height: 1.1;
  }
  .contact-role {
    font-size: 15px; color: var(--title-grey); text-transform: uppercase;
    letter-spacing: .5px; margin-bottom: 38px;
  }
  .contact-block { font-size: 15px; line-height: 1.45; margin-bottom: 24px; }
  .label { display: inline-block; width: 20px; }
</style>
</head>
<body>
  <main class="card">
    <div class="brand">
      <svg class="brand-mark" viewBox="0 0 140 140" aria-hidden="true">
        <circle cx="70" cy="70" r="68" fill="none" stroke="var(--brand-red)" stroke-width="1.5"/>
      </svg>
      <span class="brand-name">KD Velatrans</span>
    </div>
    <section class="contact">
      <h1 class="contact-name">Kelbri Dausz</h1>
      <p class="contact-role">Geschäftsführer</p>
      <p class="contact-block">Musterstraße 12<br>12345 Musterstadt</p>
      <p class="contact-block"><span class="label">T</span>01234 – 5678910<br><span class="label">M</span>0170 – 1234567</p>
      <p class="contact-block">k.dausz@kd-velatrans.com<br>www.kd-velatrans.com</p>
    </section>
  </main>
</body>
</html>
```